Website for Cuff-Tastics
Cuff-Tastics
Project: Website for Cuff-Tastics
Website for Cuff-Tastics - Retailers
Creative Brief
Retailers
Cuff-Tastics.com (pending)
The ‘Perfect Little Black Dress’.  You know when you've found it – chic, elegant, stylish and flattering! What’s not perfect is that sexy LBD’s are made for the mythical woman, the woman with toned, smooth, perfect arms. Dieting, exercise, lifting weights, toddlers and groceries and still perfection eludes us. Being a mere mortal means that changes in skin tone and muscle are inevitable. What to do? Stylish, little numbers can leave you feeling too exposed for comfort.  Dresses with sleeves are often matronly and dowdy. After years of heroic home-lab research and clumsy attempts using pantyhose as sleeves, I had a moment of pure inspiration! What women needed were flattering, interchangeable sleeves without costly, permanent dress alterations. Cuff-tastics was born. Cuff-tastics instantly make the perfect sleeveless LBD wearable by real women with real arms. That one perfect LBD is transformed into two, three, four or more little black dresses. You’re ready for a first date, a party, and a special gala event without extra effort or expense. Made from comfortable, breathable stretch fabric, Cuff-tastics are laser-cut, seamless camisoles with an array of flattering sleeve choices including mesh, lace, chiffon, fitted, and flutter three-quarters. They will become a seamless part of your wardrobe, transforming everything you own. It’s no myth that women of all ages can feel vibrant, energized, and youthful-and they can look that way too.  The key is to embrace who we are and use all the tools available to look our best and feel confident.  Cuff-tastics are sure to be an essential component of your wardrobe. We’ve earned the right to “bare” arms but we may choose not to!
Like a clean look with white space. Like prominent images. Dislike busy-ness. THE IMAGES FOR THE WEBSITE THAT WE WANT CAN BE SEEN HERE: http://qx.zp/8kTRwbnL47
black
Blue used in Logo
above header
http://www.plumerido.com/
http://www.trivok.com/
http://www.cardelune.com/
We'll forward a pdf file with content and a suggested layout. We will upgrade to a commerce site within 3 months. THE IMAGES FOR THE WEBSITE THAT WE WANT CAN BE SEEN HERE: http://qx.zp/8kTRwbnL47

```html
<!DOCTYPE html>
<html lang="en">
<head>
<meta charset="utf-8">
<title>Cuff-Tastics</title>
<link href="https://fonts.googleapis.com/css2?family=Raleway:wght@200;300;400;500&family=Open+Sans:wght@400;600&display=swap" rel="stylesheet">
<style>
  :root {
    --page-bg: #0d0d0d;
    --band: #161616;
    --footer-bg: #0a0a0a;
    --brand-teal: #95d8d3;
    --brand-ink: #1a1a1a;
    --nav-bg: rgba(20, 20, 20, 0.82);
    --text-main: #f2f2f2;
    --text-muted: #9a9a9a;
    --text-faint: #6f6f6f;
    --rule: #2a2a2a;
  }
  * { margin: 0; padding: 0; box-sizing: border-box; }
  html, body { width: 1200px; height: 756px; overflow: hidden; background: var(--page-bg); }
  .site {
    position: relative; width: 1200px; height: 756px; overflow: hidden;
    background: radial-gradient(ellipse at 55% 20%, #2a2a2a 0%, #111 55%, var(--page-bg) 100%);
    font-family: "Open Sans", Arial, sans-serif; color: var(--text-main);
  }
  .hero-photo {
    position: absolute; left: 380px; top: 0; width: 760px; height: 380px;
    background:
      radial-gradient(ellipse 22% 40% at 40% 10%, #c9a48c 0%, rgba(150,110,90,0.5) 50%, transparent 100%),
      radial-gradient(ellipse 30% 45% at 38% 60%, #2f6a72 0%, #173c44 45%, transparent 80%),
      linear-gradient(90deg, rgba(13,13,13,1) 0%, rgba(40,40,40,0.6) 30%, rgba(60,60,60,0.5) 60%, rgba(13,13,13,1) 100%);
    -webkit-mask-image: linear-gradient(180deg, #000 60%, transparent 100%);
    mask-image: linear-gradient(180deg, #000 60%, transparent 100%);
  }
  .brand-box {
    position: absolute; left: 156px; top: 12px; width: 240px; height: 173px;
    background: var(--brand-teal); display: flex; align-items: flex-end; justify-content: center;
    padding-bottom: 56px;
  }
  .brand-name {
    font-family: "Raleway", sans-serif; font-weight: 400; font-size: 19px;
    letter-spacing: 1px; color: var(--brand-ink); text-transform: uppercase;
  }
  .main-nav {
    position: absolute; left: 396px; top: 91px; width: 636px; height: 41px;
    background: var(--nav-bg);
  }
  .main-nav a {
    position: absolute; top: 14px; font-family: "Raleway", sans-serif; font-weight: 500;
    font-size: 11px; letter-spacing: 0.5px; color: var(--text-main); text-decoration: none;
  }
  .headline {
    position: absolute; left: 204px; top: 336px;
    font-family: "Raleway", sans-serif; font-weight: 200; font-size: 48px;
    letter-spacing: 2px; color: var(--text-main); white-space: nowrap;
  }
  .subline {
    position: absolute; left: 204px; top: 398px;
    font-family: "Raleway", sans-serif; font-weight: 400; font-size: 18.5px;
    color: var(--text-main); white-space: nowrap;
  }
  .intro { position: absolute; left: 204px; top: 438px; width: 420px; }
  .intro p { font-size: 12px; line-height: 16px; color: var(--text-muted); margin-bottom: 14px; }
  .cta {
    position: absolute; left: 636px; top: 440px; width: 204px; height: 148px;
    background: rgba(10,10,10,0.7); padding: 4px 10px;
    font-family: "Raleway", sans-serif; font-weight: 200; font-size: 35px; line-height: 35px;
    color: var(--text-main); text-decoration: none;
  }
  .cta svg { position: absolute; right: 8px; bottom: 14px; }
  .cta-photo {
    position: absolute; left: 846px; top: 440px; width: 138px; height: 148px;
    background: radial-gradient(ellipse at 45% 55%, #2f6c74 0%, #16363d 45%, #1c1c1c 80%);
  }
  .network-band {
    position: absolute; left: 0; top: 598px; width: 1200px; height: 62px; background: var(--band);
  }
  .network {
    position: absolute; left: 856px; top: 616px; display: flex; align-items: center; gap: 12px;
    font-size: 7px; color: var(--text-faint);
  }
  .network .dot { width: 13px; height: 13px; border-radius: 50%; background: #555; }
  .site-footer {
    position: absolute; left: 0; top: 660px; width: 1200px; height: 96px;
    background: var(--footer-bg); border-top: 1px solid var(--rule);
  }
  .copyright { position: absolute; left: 204px; top: 24px; font-size: 10px; color: var(--text-faint); }
  .footer-nav { position: absolute; right: 185px; top: 24px; display: flex; gap: 12px; }
  .footer-nav a { font-size: 10px; color: var(--text-faint); text-decoration: none; }
</style>
</head>
<body>
<div class="site">
  <div class="hero-photo" role="img" aria-label="Woman wearing a teal satin strapless dress with a delicate necklace"></div>

  <div class="brand-box"><span class="brand-name">Cuff-Tastics</span></div>

  <nav class="main-nav">
    <a href="#" style="left:26px">THE PROBLEM</a>
    <a href="#" style="left:158px">THE SO-LUTION</a>
    <a href="#" style="left:300px">THE COLLECTION</a>
    <a href="#" style="left:446px">ABOUT US</a>
    <a href="#" style="left:545px">CONTACT US</a>
  </nav>

  <h1 class="headline">feeling too exposed for comfort?</h1>
  <p class="subline">What to do? Stylish, little numbers can leave you feeling too exposed for comfort.</p>

  <div class="intro">
    <p>Dieting, exercise, lifting weights, toddlers and groceries and still perfection eludes us. Being a mere mortal means that changes in skin tone and muscle are inevitable.</p>
    <p>Cuff-tastics is here. Cuff-tastics instantly make the perfect sleeveless LBD wearable by real women with real arms. That one perfect LBD is transformed into two, three, four or more little black dresses. You're ready for a first date, a party, and a special gala event without extra effort or expense.</p>
  </div>

  <a class="cta" href="#">know more about the So-Lution here
    <svg width="10" height="18" viewBox="0 0 10 18"><path d="M1 1 L9 9 L1 17" fill="none" stroke="#f2f2f2" stroke-width="1.5"/></svg>
  </a>
  <div class="cta-photo" role="img" aria-label="Teal dress worn with black lace sleeves"></div>

  <div class="network-band"></div>
  <div class="network">
    <span>join our network</span>
    <span class="dot"></span><span class="dot"></span><span class="dot"></span>
  </div>

  <footer class="site-footer">
    <span class="copyright">© 2013 cuff-tastics</span>
    <nav class="footer-nav">
      <a href="#">The problem</a>
      <a href="#">The Solution</a>
      <a href="#">The Collection</a>
      <a href="#">About Us</a>
      <a href="#">Contact Us</a>
    </nav>
  </footer>
</div>
</body>
</html>
```